Clean Modern Skin Product branding/ label.

I need a label for a skincare line. The company is Velmora but product names will vary. A couple products to list are:
Sensitive Cleanser, Tevola, Ostiva, Malo ve, Quintel, Quintel Plus, Quintel Intense, Dovira, Ambrel and Fenwyn.

I would like the color scheme to be muted greens, grays, tourquise. The bottles are white, boston shaped with pumps, and ounces are 2, 4, 8, 16 ounces. When I choose the design, I can give you exact label sizes. Along with the ingredience already on the product label.

The look I desire is clean, minimal. A modern, organic look. Ideas that come to mind are a Ostrelle,https://www.ostrelle-beauty.example/product/1573/15501/3-step/step-2-exfoliate/clarifying-lotion-1 and the simplicity of Vo Tenn.

Both styles high light the name, in this case Velmora, and then the specific product.

My product is clean utilizing pure ingredients rather that a bunch fillers and binders. When I work with my clients I normally will say we need to "restore the balance" from over use of harsh products. That is why this lines works. It restores the skin to it's natural state. The process is simple, so I would like the label to reflect that simplicity.

Target Market(s)

Anyone with sensitive skin. So gender neutral

Industry/Entity Type

Skin Care Product

Font styles to use
Serif
Sans Serif
Decorative

Colors
acd037
33b8a4
fcfefd
85cae6
d3d3d3

Requirements
Must have
• Logo, name of product and color identity for cleanser, Active products, moisturizers
• I am thinking we could have one color for a cleanser and a space where I can put a sticker on which cleanser it is. Acne Cleasner, Sensitive Cleanser, and Cleanser.
Nice to have
• Not sure....suprise me. I would like the font to stay the same on the VELMORA, but you can change color, or color of leaf.
Should not have
• Too busy, too crowded or look like every other skincare line

```html
<!DOCTYPE html>
<html lang="en">
<head>
<meta charset="utf-8">
<title>Velmora — Quintel Intense Label</title>
<link rel="stylesheet" href="https://fonts.googleapis.com/css2?family=Cormorant+Garamond:wght@500;600&family=Gilda+Display&display=swap">
<style>
  :root {
    --page: #f7f7f7;
    --label: #3a3935;
    --ink-soft: #b8b2a1;
    --ink-bright: #f4f2eb;
    --ink-brand: #c9c8c2;
    --rule: #8f9a8c;
    --sage: 150, 176, 158;
    --sage-tint: 124, 168, 160;
  }
  * { margin: 0; padding: 0; box-sizing: border-box; }
  html, body { width: 1200px; height: 904px; overflow: hidden; background: var(--page); }
  .canvas { position: relative; width: 1200px; height: 904px; }

  .label { position: absolute; background: var(--label); overflow: hidden; }
  .label--front { left: 217px; top: 289px; width: 220px; height: 505px; }
  .label--back { left: 790px; top: 291px; width: 223px; height: 520px; }

  .copy {
    position: absolute; left: 0; right: 0; text-align: center;
    font-family: "Cormorant Garamond", serif; font-weight: 500;
    font-size: 9.5px; line-height: 12.5px; color: var(--ink-soft);
  }
  .copy p + p { margin-top: 13px; }

  .product-name {
    position: absolute; left: 0; right: 0; top: 181px; text-align: center;
    font-family: "Gilda Display", serif; font-weight: 400; font-size: 26px; line-height: 34px;
    letter-spacing: 1.5px; color: var(--ink-bright);
  }
  .product-rule {
    position: absolute; left: 94px; top: 259px; width: 33px; height: 1px; background: var(--rule);
  }
  .brand-name {
    position: absolute; left: 0; right: 0; top: 458px; text-align: center;
    font-family: "Cormorant Garamond", serif; font-weight: 600;
    font-size: 21px; letter-spacing: 0.5px; color: var(--ink-brand);
  }

  .botanical { position: absolute; }
  .botanical--top {
    left: 162px; top: 2px; width: 58px; height: 162px;
    background: radial-gradient(ellipse 50% 50% at 55% 50%, rgba(var(--sage), 0.30), rgba(var(--sage), 0.12) 55%, rgba(var(--sage), 0) 100%);
  }
  .botanical--bottom {
    left: 0; top: 272px; width: 77px; height: 150px;
    background: radial-gradient(ellipse 50% 50% at 50% 50%, rgba(var(--sage-tint), 0.30), rgba(var(--sage-tint), 0.12) 55%, rgba(var(--sage-tint), 0) 100%);
  }
  .botanical--sprig {
    left: 59px; top: 262px; width: 86px; height: 34px;
    background: radial-gradient(ellipse 50% 50% at 50% 50%, rgba(var(--sage), 0.32), rgba(var(--sage), 0.12) 55%, rgba(var(--sage), 0) 100%);
  }
</style>
</head>
<body>
<main class="canvas">

  <section class="label label--front" aria-label="Front label">
    <div class="botanical botanical--top" role="img" aria-label="Fine line drawing of a leafy branch"></div>
    <div class="copy" style="top:74px;">
      <p>text text text text<br>text text</p>
    </div>
    <h1 class="product-name">Quintel<br>Intense</h1>
    <div class="product-rule"></div>
    <div class="botanical botanical--bottom" role="img" aria-label="Fine line drawing of a leafy branch"></div>
    <div class="copy" style="top:379px;">
      <p>text text text text<br>text text text text text<br>text text text</p>
    </div>
    <div class="brand-name">Velmora</div>
  </section>

  <section class="label label--back" aria-label="Back label">
    <div class="copy" style="top:72px;">
      <p>text text text text<br>text text text text text</p>
      <p>text text text text<br>text text text text text text text<br>text text text text text<br>text text text text text text text<br>text text text text text</p>
      <p>text text texttext text text text<br>text text text text text<br>text text text</p>
    </div>
    <div class="botanical botanical--sprig" role="img" aria-label="Small fine line drawing of a flowering sprig"></div>
    <div class="copy" style="top:344px;">
      <p>Ingredients: text text text text text text<br>text text text text text text text text<br>text text text text text text text text</p>
    </div>
    <div class="copy" style="top:400px;">
      <p>weight</p>
    </div>
  </section>

</main>
</body>
</html>
```